Need a Crisps (Potato Chips in US) and Popcorns Logo, Artwork and Packaging Design

I want to package my home made crisps and popcorns. The crisps will be going by the name bumbim (Ks are capital) and the popcorns by the name bumbim (Should all be in same case, either all small or all caps - I leave it to designer's choice).

Crisps:
I want both a logo that will be associated with the product and a package design with the logo embedded. The logo should be playful and striking.

The packaging for the crisps should be to the standards of international brands like Vorn, Flumbix, Garvelo, etc. Package type is the pouch based packages.

The colours should be vibrant. We are limited to 4 colours in the design due to printing costs. So the designer should use a mixture that is striking especially to children and young adults.

Incorporation of animal artwork is allowed as long as it does not infringe on IPs.

Popcorns:
This one is less intensive and only requires a logo and package design like the one used in movie halls.

Target Market(s)

Kids and young adults

Industry/Entity Type

Food Production

Logo Text

bumbim for crisps and bumbim for popcorn

Colors

Designer to choose colors to be used in the design.

Requirements
Must have
• Playful font and colours
Nice to have
• Distinguishing artwork

```html
<!DOCTYPE html>
<html lang="en">
<head>
<meta charset="utf-8">
<title>bumbim Popcorn Pack</title>
<link rel="stylesheet" href="https://fonts.googleapis.com/css2?family=Exo+2:wght@300;400;700&display=swap">
<style>
  :root {
    --page: #ffffff;
    --pack-edge: #2a0505;
    --maroon-deep: #3a0707;
    --maroon-glow: #b8300a;
    --flame-red: #ff3c0f;
    --flame-orange: #ff8c00;
    --panel-yellow: #ffd21a;
    --panel-amber: #ff9a10;
    --royal-blue: #1c1a9c;
    --royal-blue-deep: #0e0c6a;
    --band-black: #0c0606;
    --band-yellow: #ffc400;
    --logo-cream: #f6e6b4;
    --ink-white: #ffffff;
    --kernel-cream: #efe4cc;
    --kernel-shadow: #b89a6c;
  }
  html, body {
    margin: 0;
    width: 1200px;
    height: 1200px;
    overflow: hidden;
    background: var(--page);
  }
  .canvas {
    display: block;
    width: 1200px;
    height: 1200px;
  }
  .brand-name {
    font-family: "Exo 2", sans-serif;
    font-weight: 700;
    font-size: 108px;
    fill: var(--logo-cream);
  }
  .product-type {
    font-family: "Exo 2", sans-serif;
    font-weight: 300;
    font-size: 54px;
    letter-spacing: 3px;
    fill: var(--ink-white);
  }
  .net-weight {
    font-family: "Exo 2", sans-serif;
    font-weight: 400;
    font-size: 32px;
    fill: var(--ink-white);
  }
</style>
</head>
<body>
<svg class="canvas" viewBox="0 0 1200 1200" xmlns="http://www.w3.org/2000/svg">
  <defs>
    <radialGradient id="pack-glow" cx="600" cy="480" r="620" gradientUnits="userSpaceOnUse">
      <stop offset="0" stop-color="var(--maroon-glow)"/>
      <stop offset="0.55" stop-color="#6a1208"/>
      <stop offset="1" stop-color="var(--maroon-deep)"/>
    </radialGradient>
    <linearGradient id="panel-fill" x1="0" y1="0" x2="1" y2="1">
      <stop offset="0" stop-color="var(--panel-yellow)"/>
      <stop offset="0.6" stop-color="var(--panel-amber)"/>
      <stop offset="1" stop-color="#e0500a"/>
    </linearGradient>
    <linearGradient id="pill-fill" x1="0" y1="0" x2="0" y2="1">
      <stop offset="0" stop-color="#3a38d8"/>
      <stop offset="0.5" stop-color="var(--royal-blue)"/>
      <stop offset="1" stop-color="var(--royal-blue-deep)"/>
    </linearGradient>
    <linearGradient id="ray-fill" x1="0" y1="1" x2="0" y2="0">
      <stop offset="0" stop-color="#c9a878"/>
      <stop offset="1" stop-color="#f4ead6"/>
    </linearGradient>
    <radialGradient id="kernel-fill" cx="0.45" cy="0.4" r="0.7">
      <stop offset="0" stop-color="var(--kernel-cream)"/>
      <stop offset="1" stop-color="var(--kernel-shadow)"/>
    </radialGradient>
    <clipPath id="pack-clip">
      <rect x="192" y="20" width="818" height="1160"/>
    </clipPath>
  </defs>

  <g class="pack" clip-path="url(#pack-clip)">
    <rect class="pack-ground" x="192" y="20" width="818" height="1160" fill="url(#pack-glow)"/>

    <g class="popcorn-rays" role="img" aria-label="Tapered rays filled with popped popcorn fanning upward">
      <polygon points="374,196 396,182 600,372 592,378" fill="url(#ray-fill)"/>
      <polygon points="424,146 448,136 604,368 596,372" fill="url(#ray-fill)"/>
      <polygon points="474,106 498,98 608,366 600,368" fill="url(#ray-fill)"/>
      <polygon points="526,76 550,70 612,366 604,366" fill="url(#ray-fill)"/>
      <polygon points="598,54 622,50 616,368 608,366" fill="url(#ray-fill)"/>
    </g>

    <g class="chevron-badge">
      <polyline class="chevron-outer" points="300,250 300,610 600,770 900,610 900,250"
        fill="none" stroke="var(--flame-red)" stroke-width="22" stroke-linejoin="miter"/>
      <polyline class="chevron-under" points="300,650 600,810 900,650"
        fill="none" stroke="var(--flame-orange)" stroke-width="18"/>
      <polygon class="chevron-panel" points="330,250 600,400 870,250 870,590 600,740 330,590"
        fill="url(#panel-fill)"/>
      <polyline class="chevron-rim" points="330,250 600,400 870,250"
        fill="none" stroke="var(--flame-red)" stroke-width="14"/>
      <polygon class="chevron-inline" points="362,300 600,430 838,300 838,570 600,700 362,570"
        fill="none" stroke="var(--royal-blue)" stroke-width="5"/>
    </g>

    <g class="brand-lockup">
      <rect class="brand-pill" x="382" y="412" width="436" height="126" rx="63"
        fill="url(#pill-fill)" stroke="#fff3b0" stroke-width="8"/>
      <text class="brand-name" x="600" y="508" text-anchor="middle">bumbim</text>
      <text class="product-type" x="600" y="628" text-anchor="middle">POPCORN</text>
    </g>

    <g class="diagonal-bands">
      <polygon class="band-black" points="192,672 1010,1000 1010,1066 192,744" fill="var(--band-black)"/>
      <polygon class="band-yellow" points="192,744 1010,1066 1010,1090 192,792" fill="var(--band-yellow)"/>
      <polygon class="band-blue" points="192,792 1010,1090 1010,1180 192,990" fill="var(--royal-blue)"/>
    </g>

    <path class="popcorn-bowl" role="img" aria-label="Photo of a white bowl overflowing with popcorn"
      d="M232,990 C262,930 350,884 460,864 C560,844 680,864 780,920 C880,976 960,1050 1010,1096 L1010,1180 L540,1180 Z"
      fill="url(#kernel-fill)"/>

    <text class="net-weight" x="236" y="1114">180g</text>
  </g>

  <rect class="pack-outline" x="192" y="20" width="818" height="1160" fill="none" stroke="var(--pack-edge)" stroke-width="3"/>
</svg>
</body>
</html>
```